New Tech Support Service needs a website design

We need a web design for a new product we are developing that provides tech support to consumers for a small ongoing monthly fee. We are looking for a fresh, technology look and feel. We want the site to have a tech feel - yet not intimidating. Simple and welcoming. We are in need of an initial landing page, sign on page, and a product home page.

Thank you to everyone who submitted designs. It was a very difficult decision!

Industry/Entity Type

Tech

```html
<!DOCTYPE html>
<html lang="en">
<head>
<meta charset="utf-8">
<title>brightdesk – Tech Support</title>
<link href="https://fonts.googleapis.com/css2?family=Open+Sans:wght@300;400;600&display=swap" rel="stylesheet">
<style>
:root{
  --teal:#41c6b8;
  --black:#111111;
  --white:#ffffff;
  --ink:#333333;
  --muted:#8a8a8a;
  --rule:#9a9a9a;
}
*{box-sizing:border-box;margin:0;padding:0}
html,body{width:992px;height:1200px;overflow:hidden;background:var(--white)}
body{font-family:"Open Sans",Arial,sans-serif;color:var(--ink);position:relative}
.abs{position:absolute}
.center{left:0;width:992px;text-align:center}

/* top bar */
.topbar{top:0;left:0;width:992px;height:29px;background:var(--teal);color:var(--white);font-size:11.5px}
.topbar .item{position:absolute;top:0;height:29px;line-height:29px;display:flex;align-items:center;gap:6px}
.topbar .sep{position:absolute;top:0;width:1px;height:29px;background:rgba(255,255,255,.35)}
.topbar svg{fill:var(--white)}

/* header */
.header{top:29px;left:0;width:992px;height:93px;background:var(--black)}
.logo{position:absolute;left:58px;top:32px;color:var(--white);font-weight:300;font-size:25px;line-height:30px;display:flex;align-items:center;gap:8px}
.logo .dot{width:10px;height:10px;border-radius:50%;background:var(--teal)}
.nav-rule{position:absolute;left:490px;top:30px;width:384px;height:1px;background:#555}
.nav-active{position:absolute;left:490px;top:29px;width:38px;height:2px;background:var(--teal)}
.nav a{position:absolute;top:42px;color:var(--white);font-size:11.8px;text-decoration:none;letter-spacing:.2px}
.btn-box{position:absolute;top:30px;width:39px;height:33px;background:var(--white);display:flex;align-items:center;justify-content:center}
.badge{position:absolute;left:948px;top:20px;width:14px;height:14px;border-radius:50%;background:var(--teal);color:var(--white);font-size:9px;line-height:14px;text-align:center}

/* hero */
.hero{top:122px;left:0;width:992px;height:413px;background:radial-gradient(ellipse at 50% 15%,#e9e5dc 0%,#bdb6aa 30%,#6f6b69 60%,#3a3d45 100%)}
.hero-photo{position:absolute;inset:0;background:linear-gradient(90deg,rgba(150,90,50,.35),rgba(0,0,0,0) 30%,rgba(0,0,0,0) 70%,rgba(40,45,60,.4))}
.hero h1{position:absolute;top:52px;font-weight:300;font-size:29.5px;line-height:33px;color:#1a1a1a}
.hero p{position:absolute;top:134px;font-size:11px;line-height:16px;color:#222}
.arrow{position:absolute;top:164px;width:32px;height:32px;border-radius:50%;background:rgba(40,40,40,.75);display:flex;align-items:center;justify-content:center}
.solution{position:absolute;top:240px;width:260px;text-align:center;color:var(--white)}
.solution .icon-area{width:136px;height:92px;margin:0 auto;border-radius:6px;background:rgba(255,255,255,.14)}
.solution span{display:block;font-weight:300;font-size:24px;line-height:30px;margin-top:6px}
.dots{position:absolute;top:388px;left:448px;display:flex;gap:5px}
.dots i{width:17px;height:16px;border:2px solid var(--white);display:block}
.dots i.on{background:var(--teal)}
.dots i.off{border-color:#777}

/* welcome */
.welcome{top:535px;left:0;width:992px;height:207px;background:var(--teal);color:var(--white)}
.welcome h2{position:absolute;top:33px;font-weight:300;font-size:22px;line-height:30px}
.welcome .rule{position:absolute;top:69px;left:202px;width:588px;height:1px;background:rgba(255,255,255,.7)}
.welcome .rule-mid{position:absolute;top:69px;left:354px;width:273px;height:2px;background:var(--white)}
.welcome .lead{position:absolute;top:90px;left:100px;width:792px;text-align:center;font-size:12.3px;line-height:17px}
.welcome .body{position:absolute;top:133px;left:80px;width:832px;text-align:center;font-size:10.6px;line-height:16.5px}

/* support section */
.support h3{position:absolute;top:776px;font-weight:300;font-size:19.8px;line-height:28px;color:#222}
.support .rule{position:absolute;top:810px;left:63px;width:888px;height:1px;background:var(--rule)}
.support .intro{position:absolute;top:824px;left:90px;width:812px;text-align:center;color:var(--teal);font-size:11.6px;line-height:16.5px}
.laptop{position:absolute;left:50px;top:893px;width:330px;height:264px;background:linear-gradient(160deg,#ffffff 0%,#3a3a4c 35%,#2a2a30 60%,#d07434 80%,#ffffff 100%);opacity:.9}
.features{position:absolute;left:434px;top:889px;width:514px;list-style:none}
.features li{position:relative;padding-left:24px;margin-bottom:9px}
.features svg{position:absolute;left:0;top:4px}
.features h4{font-weight:400;font-size:15px;line-height:20px;color:#222}
.features p{font-size:10.3px;line-height:15.8px;color:var(--muted)}
.footer-band{position:absolute;top:1190px;left:0;width:992px;height:10px;background:var(--black)}
</style>
</head>
<body>

<div class="abs topbar">
  <div class="item" style="left:18px">
    <svg width="11" height="11" viewBox="0 0 24 24"><path d="M6.6 10.8a15.1 15.1 0 0 0 6.6 6.6l2.2-2.2a1 1 0 0 1 1-.25 11.4 11.4 0 0 0 3.6.57 1 1 0 0 1 1 1V20a1 1 0 0 1-1 1A17 17 0 0 1 3 4a1 1 0 0 1 1-1h3.5a1 1 0 0 1 1 1c0 1.25.2 2.45.57 3.57a1 1 0 0 1-.25 1z"/></svg>
    <span>0123-456-789</span>
  </div>
  <div class="sep" style="left:124px"></div>
  <div class="item" style="left:137px">
    <svg width="11" height="9" viewBox="0 0 24 18"><path d="M0 0h24v2L12 10 0 2z M0 5l12 8 12-8v13H0z"/></svg>
    <span>sales@yourcompany.com</span>
  </div>
  <div class="item" style="left:617px">Sign in</div>
  <div class="sep" style="left:667px"></div>
  <div class="item" style="left:683px">Sign up</div>
  <div class="sep" style="left:736px"></div>
  <div class="item" style="left:743px">Language -
    <svg width="12" height="8" viewBox="0 0 12 8"><rect width="12" height="8" fill="#ffffff" opacity=".8"/></svg>
    <svg width="8" height="5" viewBox="0 0 8 5"><path d="M0 0h8L4 5z"/></svg>
  </div>
  <div class="sep" style="left:846px"></div>
  <div class="item" style="left:856px"><svg width="10" height="11" viewBox="0 0 10 11"><circle cx="5" cy="3" r="2.6"/><path d="M0 11c0-3 2-5 5-5s5 2 5 5z"/></svg></div>
  <div class="sep" style="left:876px"></div>
  <div class="item" style="left:886px"><svg width="11" height="10" viewBox="0 0 24 22"><path d="M12 22 2 12A6 6 0 0 1 12 3a6 6 0 0 1 10 9z"/></svg></div>
  <div class="sep" style="left:906px"></div>
  <div class="item" style="left:916px"><svg width="9" height="11" viewBox="0 0 9 11"><rect y="5" width="9" height="6"/><path d="M2 5V3a2.5 2.5 0 0 1 5 0v2H6V3a1.5 1.5 0 0 0-3 0v2z"/></svg></div>
  <div class="sep" style="left:936px"></div>
  <div class="item" style="left:947px"><svg width="10" height="11" viewBox="0 0 10 11"><circle cx="5" cy="3" r="2.6"/><path d="M0 11c0-3 2-5 5-5s5 2 5 5z"/></svg></div>
</div>

<header class="abs header">
  <div class="logo"><span class="dot"></span>brightdesk</div>
  <div class="nav-rule"></div>
  <div class="nav-active"></div>
  <nav class="nav">
    <a href="#" style="left:491px">HOME</a>
    <a href="#" style="left:559px">PRODUCTS</a>
    <a href="#" style="left:647px">SERVICES</a>
    <a href="#" style="left:734px">BLOG</a>
    <a href="#" style="left:798px">CONTACT US</a>
  </nav>
  <div class="btn-box" style="left:882px">
    <svg width="13" height="13" viewBox="0 0 14 14" fill="none" stroke="#555" stroke-width="2"><circle cx="6" cy="6" r="4.5"/><path d="M9.5 9.5 13 13"/></svg>
  </div>
  <div class="btn-box" style="left:930px;width:37px">
    <svg width="16" height="14" viewBox="0 0 16 14" fill="#111"><path d="M0 0h3l.6 2H16l-2 6H5l.5 1.5H14V11H4.3L1.8 1.5H0z"/><circle cx="5.5" cy="12.8" r="1.2"/><circle cx="12.5" cy="12.8" r="1.2"/></svg>
  </div>
  <div class="badge">0</div>
</header>

<section class="abs hero">
  <div class="hero-photo" role="img" aria-label="Soft blurred background photo in warm amber and slate tones"></div>
  <h1 class="center">More than half a decade<br>of simplifying technology for the world</h1>
  <p class="center">Because we never know what problem a customer might face, we make sure we are equipped to handle everything. Every single thing.<br>Just call us, and watch your problem become ours.</p>
  <div class="arrow" style="left:6px"><svg width="10" height="14" viewBox="0 0 10 14" fill="none" stroke="#fff" stroke-width="2"><path d="M8 1 2 7l6 6"/></svg></div>
  <div class="arrow" style="left:949px"><svg width="10" height="14" viewBox="0 0 10 14" fill="none" stroke="#fff" stroke-width="2"><path d="M2 1l6 6-6 6"/></svg></div>

  <div class="solution" style="left:22px">
    <div class="icon-area" role="img" aria-label="Line illustration of a house inside a cloud"></div>
    <span>Home Solutions</span>
  </div>
  <div class="solution" style="left:358px">
    <div class="icon-area" role="img" aria-label="Line illustration of a rising chart inside a circle"></div>
    <span>Business Solutions</span>
  </div>
  <div class="solution" style="left:688px">
    <div class="icon-area" role="img" aria-label="Line illustration of a gear inside a cloud"></div>
    <span>Enterprise Solutions</span>
  </div>
  <div class="dots"><i class="on"></i><i></i><i></i><i class="off"></i></div>
</section>

<section class="abs welcome">
  <h2 class="center">WELCOME, HELLO WORLD!</h2>
  <div class="rule"></div>
  <div class="rule-mid"></div>
  <p class="lead">Lorem ipsum dolor sit amet, consectetur adipiscing elit. Donec id lacus nunc. Etiam tincidunt lorem ac diam tristique, eget ultrices eros ornare. Mauris vel arcu neque.</p>
  <p class="body">Maecenas mauris velit, consequat sit amet pharetra ut, ultricies vitae mi. Duis tempus mattis sem id placerat. Sed et risus non erat feugiat tempus in sed arcu.<br>Mauris eu sem purus.Lorem ipsum dolor sit amet, consectetur adipiscing elit. Ut at fringilla libero. Nam justo sem,<br>porttitor eget dapibus id, fringilla sit amet massa. Donec vulputate molestie</p>
</section>

<section class="support">
  <h3 class="abs center">Work faster on your Laptop with support from us. Call toll free 1 800 123 4567.</h3>
  <div class="rule"></div>
  <p class="intro">Over time, old files build up on your hard drive and all the adding and removing of software leaves behind quite a mess. All these factors reduce the efficiency of your computer, which means you don't get the performance you deserve.</p>
  <div class="laptop" role="img" aria-label="Photo of a convertible laptop with an orange frame shown in several folding positions"></div>
  <ul class="features">
    <li>
      <svg width="14" height="14" viewBox="0 0 14 14"><circle cx="7" cy="7" r="7" fill="#41c6b8"/><path d="M4 7.2 6.2 9.3 10 5" fill="none" stroke="#fff" stroke-width="1.8"/></svg>
      <h4>Make Your Computer Work Like New</h4>
      <p>tech experts speed up your computer by removing junk files, fixing Registry errors, defragment-ing the hard disk, etc.</p>
    </li>
    <li>
      <svg width="14" height="14" viewBox="0 0 14 14"><circle cx="7" cy="7" r="7" fill="#41c6b8"/><path d="M4 7.2 6.2 9.3 10 5" fill="none" stroke="#fff" stroke-width="1.8"/></svg>
      <h4>Faster Booting and Shutdown</h4>
      <p>System tweaks reduce your computer's start-up and shutdown time and you will find that applica-tions run better.</p>
    </li>
    <li>
      <svg width="14" height="14" viewBox="0 0 14 14"><circle cx="7" cy="7" r="7" fill="#41c6b8"/><path d="M4 7.2 6.2 9.3 10 5" fill="none" stroke="#fff" stroke-width="1.8"/></svg>
      <h4>Optimize the Performance</h4>
      <p>The technicians will delete unwanted files and remove unnecessary background processes to get the best out of the hardware and software.</p>
    </li>
    <li>
      <svg width="14" height="14" viewBox="0 0 14 14"><circle cx="7" cy="7" r="7" fill="#41c6b8"/><path d="M4 7.2 6.2 9.3 10 5" fill="none" stroke="#fff" stroke-width="1.8"/></svg>
      <h4>Update Software and Drivers</h4>
      <p>Outdated/corrupted applications or drivers can slow down your computer. Let our technicians download the latest versions and update them for optimum performance. - See more at: http://www.brightdesk-help.com/services/tune-up.html</p>
    </li>
  </ul>
</section>

<div class="footer-band"></div>
</body>
</html>
```